Stationary for New Company

We need stationary designed for a new company. Details of the required stationary is attached.

The final version should be trendy, clean... only 2 colours (green + grey/black) and professional.

#1: Business Cards (design on 2 sides)
#2: Letterhead (word format)
#3: Cover Page and back cover for proposals
#4: Envelopes,
#5: Thank You card,
#6: Presentation Folder,
#7: Email signatures template (sample attached in word document)

Logo is attached. Logo can be reversed out (will attach once available). Logo can be stacked or horizontal (provided as horizontal).

Files need to be provided in ai + png format.

Target Market(s)

Business owners. More affluent.

Industry/Entity Type

Business

Requirements
Must have
• See brief

Font: Calibri
Should not have
• Photographs / stock photos

```html
<!DOCTYPE html>
<html lang="en">
<head>
<meta charset="utf-8">
<title>Northgate Insurance Brokers – Thank You Card</title>
<link rel="stylesheet" href="https://fonts.googleapis.com/css2?family=Carlito:wght@400;700&family=Pinyon+Script&display=swap">
<style>
  :root {
    --backdrop: #5b5b5b;
    --paper: #ffffff;
    --brand-green: #557a18;
    --brand-green-deep: #4b7112;
    --brand-grey: #808080;
    --text-grey: #6e6e6e;
    --ghost: rgba(255, 255, 255, 0.12);
  }
  * { margin: 0; padding: 0; box-sizing: border-box; }
  html, body {
    width: 1200px;
    height: 1000px;
    overflow: hidden;
    background: var(--backdrop);
  }
  .thank-you-card {
    position: absolute;
    left: 249px;
    top: 250px;
    width: 710px;
    height: 496px;
    background: var(--paper);
    overflow: hidden;
    font-family: "Carlito", Arial, sans-serif;
  }
  .brand {
    position: absolute;
    left: 55px;
    top: 50px;
    display: flex;
    align-items: center;
    gap: 13px;
  }
  .brand-square {
    width: 62px;
    height: 70px;
    background: var(--brand-green);
  }
  .brand-name {
    color: var(--text-grey);
    font-weight: 400;
    line-height: 1;
  }
  .brand-name .primary { display: block; font-size: 38px; letter-spacing: -0.5px; }
  .brand-name .secondary { display: block; font-size: 17px; margin-top: 3px; padding-left: 2px; }
  .contact {
    position: absolute;
    right: 55px;
    top: 71px;
    text-align: right;
    font-family: Arial, "Carlito", sans-serif;
    font-size: 11px;
    line-height: 13.5px;
    color: var(--text-grey);
  }
  .contact .label { color: var(--brand-green); font-weight: 700; }
  .contact .web-name { color: var(--brand-green); font-weight: 700; }
  .divider { position: absolute; top: 161px; height: 15px; }
  .divider-grey { left: 0; width: 354px; background: var(--brand-grey); }
  .divider-tick { width: 3px; background: var(--brand-green); }
  .divider-tick.first { left: 359px; }
  .divider-tick.second { left: 365px; }
  .divider-green { left: 373px; right: 0; background: var(--brand-green); }
  .message-panel {
    position: absolute;
    left: 0;
    right: 0;
    top: 186px;
    bottom: 0;
    background: linear-gradient(180deg, var(--brand-green) 0%, var(--brand-green-deep) 100%);
  }
  .ghost-square {
    position: absolute;
    left: 512px;
    top: 49px;
    width: 174px;
    height: 237px;
    background: var(--ghost);
  }
  .greeting {
    position: absolute;
    left: 58px;
    top: 40px;
    font-family: "Pinyon Script", cursive;
    color: var(--paper);
    font-weight: 400;
    line-height: 1;
  }
  .greeting .line { display: block; font-size: 118px; }
  .greeting .line-two { margin-left: 100px; margin-top: -18px; }
</style>
</head>
<body>
  <article class="thank-you-card">
    <header class="card-header">
      <div class="brand">
        <div class="brand-square"></div>
        <div class="brand-name">
          <span class="primary">Northgate</span>
          <span class="secondary">Insurance Brokers</span>
        </div>
      </div>
      <address class="contact">
        2280 Maple Ridge Road, Calgary, AB&nbsp; T2X 4K8<br>
        <span class="label">Phone:</span> 555.210.4400 · <span class="label">Fax:</span>&nbsp; 555.210.4401<br>
        www.<span class="web-name">northgatebrokers</span>.com
      </address>
    </header>
    <div class="divider divider-grey"></div>
    <div class="divider divider-tick first"></div>
    <div class="divider divider-tick second"></div>
    <div class="divider divider-green"></div>
    <section class="message-panel">
      <div class="ghost-square"></div>
      <h1 class="greeting">
        <span class="line">Thank</span>
        <span class="line line-two">you!</span>
      </h1>
    </section>
  </article>
</body>
</html>
```